Wren's Home Care Retractable Banner Design

Retractable Banner Design
We need a pull up retractable banner design
85 x 206 cm.
We need the banner to use at expo's, information sessions, presentations, recruitment days. Needs to be attractive to our elderly client's and staff (care workers)
Phone number needs to be on 08 7394 2650
Website also needs to be on the banner : wrenshomecare-example.com.au

Target Market(s)

35 +

Industry/Entity Type

aged care / community

Requirements
Must have
• Colours, fonts and logo as detailed in upload

```html
<!DOCTYPE html>
<html lang="en">
<head>
<meta charset="utf-8">
<title>Wren's Home Care – Pull-up Banner</title>
<link rel="stylesheet" href="https://fonts.googleapis.com/css2?family=Poppins:wght@400;600;700&display=swap">
<style>
  :root {
    --page-bg: #d9d7d7;
    --banner-bg: #e9e8e8;
    --brand-red: #8e1a2e;
    --brand-red-bright: #a71d2e;
    --brand-red-deep: #4a0008;
    --heading-grey: #3a3a3a;
    --body-grey: #444444;
    --white: #ffffff;
  }
  html, body {
    margin: 0;
    padding: 0;
    width: 1200px;
    height: 2566px;
    overflow: hidden;
    background: var(--page-bg);
    font-family: "Poppins", sans-serif;
  }
  .canvas {
    position: relative;
    width: 1200px;
    height: 2566px;
  }
  .banner {
    position: absolute;
    left: 75px;
    top: 75px;
    width: 1080px;
    height: 2430px;
    background: var(--banner-bg);
    overflow: hidden;
  }
  .banner-art {
    position: absolute;
    inset: 0;
  }
  .brand-badge {
    position: absolute;
    left: 105px;
    top: 970px;
    width: 440px;
    height: 440px;
    border-radius: 50%;
    background: var(--white);
    border: 22px solid var(--brand-red-bright);
    box-sizing: border-box;
    display: flex;
    align-items: center;
    justify-content: center;
    box-shadow: 0 40px 40px -20px rgba(0,0,0,0.25);
  }
  .brand-name {
    margin: 0;
    font-weight: 600;
    font-size: 44px;
    line-height: 1.1;
    color: var(--brand-red);
    text-align: center;
  }
  .headline {
    position: absolute;
    left: 97px;
    top: 1530px;
    margin: 0;
    font-weight: 700;
    line-height: 1;
    white-space: nowrap;
  }
  .headline-accent {
    display: block;
    font-size: 112px;
    color: var(--brand-red);
  }
  .headline-main {
    display: block;
    font-size: 112px;
    color: var(--heading-grey);
    margin-top: 8px;
  }
  .intro {
    position: absolute;
    left: 97px;
    top: 1798px;
    width: 860px;
    margin: 0;
    font-size: 34px;
    line-height: 62px;
    color: var(--body-grey);
    white-space: nowrap;
  }
  .contact {
    position: absolute;
    left: 97px;
    display: flex;
    align-items: center;
  }
  .contact-phone { top: 2047px; }
  .contact-web { top: 2203px; }
  .contact-icon {
    position: relative;
    z-index: 1;
    flex: none;
    width: 128px;
    height: 124px;
    border-radius: 14px;
    border: 2px solid var(--brand-red-bright);
    box-sizing: border-box;
    padding: 6px;
  }
  .contact-icon-inner {
    width: 100%;
    height: 100%;
    border-radius: 10px;
    background: linear-gradient(135deg, var(--brand-red) 0%, var(--brand-red-bright) 100%);
    display: flex;
    align-items: center;
    justify-content: center;
  }
  .contact-pill {
    flex: none;
    margin-left: -6px;
    height: 86px;
    border-radius: 0 24px 24px 0;
    background: var(--brand-red);
    color: var(--white);
    font-weight: 700;
    display: flex;
    align-items: center;
    box-sizing: border-box;
    white-space: nowrap;
    overflow: hidden;
  }
  .contact-phone .contact-pill { width: 429px; padding-left: 44px; font-size: 46px; }
  .contact-web .contact-pill { width: 640px; padding-left: 24px; font-size: 34px; font-weight: 600; }
</style>
</head>
<body>
<div class="canvas">
  <section class="banner">
    <svg class="banner-art" width="1080" height="2430" viewBox="0 0 1080 2430">
      <defs>
        <linearGradient id="photoTone" x1="0" y1="0" x2="1" y2="1">
          <stop offset="0" stop-color="#8d8279"/>
          <stop offset="0.5" stop-color="#a9a49d"/>
          <stop offset="0.8" stop-color="#7fa596"/>
          <stop offset="1" stop-color="#2a2a2a"/>
        </linearGradient>
        <linearGradient id="waveBand" x1="0" y1="0" x2="1" y2="1">
          <stop offset="0" stop-color="#6a1020"/>
          <stop offset="0.45" stop-color="#3e0006"/>
          <stop offset="0.7" stop-color="#a71d2e"/>
          <stop offset="1" stop-color="#2b0a10"/>
        </linearGradient>
        <linearGradient id="waveSheen" x1="0" y1="0" x2="1" y2="0">
          <stop offset="0" stop-color="#8a6a70"/>
          <stop offset="1" stop-color="#d8c8cb"/>
        </linearGradient>
      </defs>
      <path role="img" aria-label="Photo: a carer embracing an elderly woman seated on a sofa at home"
            d="M0,0 H1080 V825 C925,935 625,935 425,825 C275,745 125,665 0,605 Z"
            fill="url(#photoTone)"/>
      <path class="wave-band"
            d="M0,605 C125,665 275,745 425,825 C625,935 925,935 1080,825 V1795 C925,1625 825,1525 725,1485 C625,1425 575,1305 505,1175 C405,985 225,885 0,815 Z"
            fill="url(#waveBand)"/>
      <path class="wave-sheen"
            d="M0,605 C125,665 275,745 425,825 C625,935 925,935 1080,825 V870 C925,990 625,990 425,880 C275,800 125,720 0,660 Z"
            fill="url(#waveSheen)" opacity="0.85"/>
      <path class="wave-stripe" d="M0,700 C200,790 400,900 600,1000 C800,1090 950,1130 1080,1180"
            fill="none" stroke="#c8263a" stroke-width="6"/>
      <path class="wave-stripe" d="M0,760 C250,850 450,960 650,1120 C820,1250 950,1300 1080,1340"
            fill="none" stroke="#b51f33" stroke-width="10"/>
      <path class="wave-stripe" d="M520,1260 C600,1400 680,1470 810,1455"
            fill="none" stroke="#cfe3da" stroke-width="5"/>
      <path class="wave-stripe" d="M540,1300 C640,1500 800,1560 945,1335"
            fill="none" stroke="#3a0a12" stroke-width="4"/>
    </svg>

    <div class="brand-badge">
      <p class="brand-name">Wren's<br>Home Care</p>
    </div>

    <h1 class="headline">
      <span class="headline-accent">Caring</span>
      <span class="headline-main">for Your Loved</span>
    </h1>

    <p class="intro">Lorem ipsum dolor sit amet, consectetuer,<br>sed diam nonummy nibh euismod tincidunt ut<br>laoreet dolore magna aliquam erat</p>

    <div class="contact contact-phone">
      <div class="contact-icon">
        <div class="contact-icon-inner">
          <svg width="52" height="52" viewBox="0 0 24 24" aria-hidden="true">
            <path d="M6.6 10.8a15.1 15.1 0 0 0 6.6 6.6l2.2-2.2a1 1 0 0 1 1-.25 11.4 11.4 0 0 0 3.6.57 1 1 0 0 1 1 1V20a1 1 0 0 1-1 1A17 17 0 0 1 3 4a1 1 0 0 1 1-1h3.5a1 1 0 0 1 1 1c0 1.25.2 2.45.57 3.57a1 1 0 0 1-.25 1z" fill="#fff"/>
            <path d="M14 3.5a6.5 6.5 0 0 1 6.5 6.5M14 6.5a3.5 3.5 0 0 1 3.5 3.5" fill="none" stroke="#fff" stroke-width="1.6" stroke-linecap="round"/>
          </svg>
        </div>
      </div>
      <div class="contact-pill">08 7394 2650</div>
    </div>

    <div class="contact contact-web">
      <div class="contact-icon">
        <div class="contact-icon-inner">
          <svg width="52" height="56" viewBox="0 0 24 26" aria-hidden="true">
            <path d="M12 1a7 7 0 0 0-7 7c0 5 7 12 7 12s7-7 7-12a7 7 0 0 0-7-7zm0 9.5A2.5 2.5 0 1 1 12 5.5a2.5 2.5 0 0 1 0 5z" fill="#fff"/>
            <ellipse cx="12" cy="22.5" rx="8" ry="2.5" fill="#fff"/>
          </svg>
        </div>
      </div>
      <div class="contact-pill">wrenshomecare-example.com.au</div>
    </div>
  </section>
</div>
</body>
</html>
```